依頼詳細
概要、特徴にも書いたように、今回、分離発注に向けた営業用のチラシを作成して頂きたいです。

・すでに既存で新規顧客獲得用のパンフレット(高難度松浦工業)とチラシ(HARUKAZE)があり、今回は、それらに追加で挟む “分離発注を目的としたチラシ” の依頼となります。

※既存(高難度パンフレット)(添付資料1、2)
+
既存(HARUKAZE)(添付資料3)
+
“分離発注を目的としたチラシ”

既存の3つのチラシ(※添付資料1.2.3)と一緒に挟んで、配布したいので

流れを理解して作成していただけたら幸いです。

・流れ、
株式会社松浦工業は、高難度の足場を専門で営業しています。

また、その職人で構成されている、HARUKAZEというワンランク上の足場サービスも運営しています。(住人さんや近隣様、などへの配慮、最高のサービスを提供するブランド)
(HARUKAZEにもホームページがございます。)

安全には、費用がかかります。
人の命は尊いです。
工事は足場から始まり、足場で終わります。
そして、業者みんなが使う足場です。

弊社の売りを武器として運営し維持して行くためには、無駄な予算を削り、その予算を安心できる工事に生かす。

そして見た目も美しい職人で揃えている私たちと手を組みませんか。

。。。といった流れでイメージして作成して頂きたいです。

※弊社の売りに関しましては、添付した資料やホームページを確認して頂き、理解して頂きたいです。

・目的は、新規顧客の獲得ですが、分離発注の提案を載せたいです。

・新規顧客(ターゲット)→ビル建物のオーナー、元請業社、ゼネコンなど

・メリットとデメリットをまとめたマインドマップも添付しますので、必要であれば使ってください。
・他にも、ホームページもありますので、見ていただけたら、と思います。
・弊社は改修工事用の足場をメインで運営しております。
(居住者様や、近隣様、歩行者様からの安心や業者間、現場管理監督様とのコミュニケーションもとても大切にしております。)
・メリットのマインドマップの他にも、弊社を使うことでのメリットは、たくさんあります。
・どの立場から見ても美しい足場屋を目指しております。

記載項目
分離発注しませんか。

株式会社松浦工業
042−718−2964
https://matsuurakogyo-ashiba.example
↑↑
株式会社松浦工業(高難度専門の足場サービス)

https://harukaze-ashiba.example
↑↑
ワンランク上の足場サービス
HARUKAZE ホームページ

サイズ
A4
ページ数
両面
希望イメージ
シンプル 複雑
単色 カラフル
暗い 明るい
日常 高級
遊び心 厳粛
未来的 伝統的
女性的 男性的
希望する色
黄・オレンジ系、緑系、青系、既存チラシ(添付資料1.2.3)とのバランスで決めて頂きたい
納品ファイル
• 高解像度JPG (.jpg)
• イラストレーター形式 (.ai)
補足説明
↑↑
株式会社松浦工業(高難度専門の足場サービス)

↑↑
ワンランク上の足場サービス
HARUKAZE ホームページ

どちらも並行して運営しております!

ーーーーーーーーーーーーーーーーーーーーーーーーー

※多少の文字の変更などがしやすいように、アウトライン化されていないデータでも納品して頂きたいです。
みなさま、すばらしい作品をありがとうございます!

みなさまの作品を見て間違えに気づくことが出来ました。

一部、変更させてください!

3点あるのですが、

①1つ目は、このチラシを誰に当てた手紙にするのか、ですが、ターゲットは、
・ビルやマンション、学校など建物のオーナー様
・ビルやマンションの管理をしている管理会社様や、
・不動産会社様
・店舗、等の工事担当者様
に当てた手紙で作成して頂きたいです。

※よく考えたら工事会社が直接足場屋に依頼するのは、当前のことだと思いましたので、工事業者に当てるのはおかしい話だと気付いたので宜しくお願いいたします。

②見積もり依頼までの流れを盛り込んで頂きたいです。
流れ
平日の9:00〜17:00に
042−718−2964

に電話をして頂き、弊社の電話に出た物に、見積もりして欲しい物件のご住所をお聞かせください。

or

当社ホームページ問い合わせフォームのQRコード?
かURL??

で見積もり依頼のメッセージを頂けたら、

1週間以内にTerravue Mapsを元に概算でお見積もりして郵送させて頂きます。

※建物の改修工事が決まりましたら、弊社と工事業者様とで直接お打ち合わせして、施工します!
※安心、安全へのクオリティは、高品質をお約束しますので、安心してください。
※足場工事は、命の危険を伴う工事です。

。。。のような感じをうまく刺さる形で表現して頂きたいです。

③ターゲットに分離発注という意味を理解してもらえるのかも不安になってきたのですが、どうでしょうか。

このチラシに足場だけを分離発注しませんか?なのか、
直接発注しませんか、なのか、何か良い表現があればそれも考えていただけると幸いです。

分離発注でわかるから大丈夫だよ、であれば分離発注も構いません。
ただ僕が不安になっただけなので、
そこも何か良い案があればなーと思ったので、宜しくお願いいたします。

コロナで、大ダメージを受けてしまったので、これで、復活したいと考えております!

みなさま、どうか宜しくお願いいたします!

弊社の既存のパンフレットと一緒に配ることを踏まえてこの作品が一番良いのではないかと感じました。

この度は、本当にありがとうございました。
僕たちは、職人さん達の生活がもっと潤っていけるように、したいと考えております。
職人さん達の世界では土曜も仕事をすることが当たり前となっております。
しかし僕たちは価値の高い仕事を社会に広めていき、みんなが、より良い工事をしながら、生活も潤っていけるように考えております。
皆さんが作ってくれた作品から、僕たちは大きな気づきをゲットしました!
とても感謝しています。
本当に本当にありがとうございました。

```html
<!DOCTYPE html>
<html lang="ja">
<head>
<meta charset="utf-8">
<title>分離発注のご案内｜株式会社松浦工業</title>
<link rel="stylesheet" href="https://fonts.googleapis.com/css2?family=Noto+Sans+JP:wght@400;500;700;900&display=swap">
<style>
  :root{
    --ink:#1f2226;
    --paper:#ffffff;
    --accent:#e9a23b;
    --photo-dark:#2b2f35;
    --photo-mid:#4a5058;
    --photo-light:#7d838b;
    --muted:#5a5e63;
  }
  *{margin:0;padding:0;box-sizing:border-box}
  html,body{width:848px;height:1200px;overflow:hidden;background:var(--paper)}
  body{font-family:"Noto Sans JP",sans-serif;color:var(--ink);position:relative}

  .hero-photo{
    position:absolute;left:0;top:0;width:848px;height:755px;
    background:
      radial-gradient(ellipse at 60% 30%, rgba(125,131,139,.55), transparent 60%),
      linear-gradient(180deg,var(--photo-mid) 0%,var(--photo-dark) 55%,#3a3f46 100%);
  }
  .gear-photo{
    position:absolute;left:430px;top:718px;width:418px;height:482px;
    background:
      radial-gradient(ellipse at 55% 45%, #9aa0a6 0%, #5b6168 55%, #33373c 100%);
  }

  .tagline{
    position:absolute;top:52px;right:50px;
    writing-mode:vertical-rl;
    font-size:30px;font-weight:500;letter-spacing:.14em;color:var(--paper);
  }
  .tagline-sub{
    position:absolute;top:58px;right:102px;
    writing-mode:vertical-rl;
    font-size:13px;line-height:1.7;letter-spacing:.1em;color:var(--accent);
  }

  .lead{
    position:absolute;left:84px;top:278px;
    font-size:21px;font-weight:500;line-height:1.6;color:var(--paper);letter-spacing:.04em;
  }
  .headline{
    position:absolute;left:80px;top:410px;color:var(--paper);line-height:1;
  }
  .headline .main{font-size:70px;font-weight:900;letter-spacing:.02em}
  .headline .particle{font-size:42px;font-weight:700}
  .headline .sub{display:block;font-size:40px;font-weight:700;margin-top:14px;letter-spacing:.06em}

  .merits{position:absolute;left:62px;top:545px;display:flex;gap:30px;list-style:none}
  .merit{
    width:84px;height:84px;border:1.5px solid var(--paper);border-radius:50%;
    display:flex;align-items:center;justify-content:center;text-align:center;
    font-size:11px;line-height:1.45;color:var(--paper);
  }

  .company{position:absolute;left:84px;top:780px;width:330px}
  .company .service{font-size:20px;font-weight:700;letter-spacing:.05em}
  .company .roman{margin-top:14px;font-size:13px;color:var(--accent);letter-spacing:.05em}
  .company .name{font-size:32px;font-weight:700;letter-spacing:.04em;margin-top:2px}
  .company .address{font-size:10px;color:var(--muted);margin-top:6px}
  .contact{display:flex;gap:14px;margin-top:6px;font-size:17px;font-weight:500;align-items:center}
  .contact span{display:flex;align-items:center;gap:4px}
  .contact svg{width:15px;height:15px}
  .company .hours{font-size:10px;color:var(--muted);margin-top:2px}
  .company .url{font-size:17px;font-weight:500;margin-top:30px;letter-spacing:.01em}
  .company .note{font-size:11px;line-height:1.6;margin-top:40px;color:var(--muted)}
</style>
</head>
<body>
  <div class="hero-photo" role="img" aria-label="安全帯と工具を腰に付けた足場職人の作業姿（暗いトーンの写真）"></div>
  <div class="gear-photo" role="img" aria-label="足場の上に置かれた安全帯と工具一式の写真"></div>

  <p class="tagline">安全な現場は美しい</p>
  <p class="tagline-sub">それぞれの専門業者へ直接発注することで、<br>コストを抑えて安全な足場が実現できます。</p>

  <p class="lead">コストを抑えながら<br>究極まで安全と安心を追求した<br>仮設足場のため</p>

  <h1 class="headline"><span class="main">分離発注</span><span class="particle">の</span><span class="sub">ご案内</span></h1>

  <ul class="merits">
    <li class="merit">不明瞭な<br>コスト削減</li>
    <li class="merit">品質・安全性<br>の向上</li>
    <li class="merit">現場による<br>工程の短縮</li>
  </ul>

  <section class="company">
    <p class="service">高難度の仮設足場承ります</p>
    <p class="roman">matsuura corporation</p>
    <p class="name">株式会社松浦工業</p>
    <p class="address">〒194-0000 東京都町田市桜台1-2-3 松浦ビル1階</p>
    <p class="contact">
      <span><svg viewBox="0 0 24 24"><circle cx="12" cy="12" r="11" fill="none" stroke="currentColor" stroke-width="2"/><path d="M8 6l2 3-1.5 1.5a8 8 0 0 0 5 5L15 14l3 2-1 2.5c-5 0-10-5-10-10z" fill="currentColor"/></svg>042-718-2964</span>
      <span><svg viewBox="0 0 24 24"><rect x="4" y="8" width="16" height="11" fill="none" stroke="currentColor" stroke-width="2"/><rect x="7" y="3" width="10" height="5" fill="none" stroke="currentColor" stroke-width="2"/></svg>042-718-2965</span>
    </p>
    <p class="hours">【受付時間】平日 9:00〜17:00</p>
    <p class="url">https://matsuurakogyo-ashiba.example</p>
    <p class="note">改修・ワクビ・外装の足場、イレギュラー仮設足場も<br>お任せください</p>
  </section>
</body>
</html>
```